bRv Design Group - architect web site

need a web site to permit potential clients to view our portfolio of work.

Will need lots of photos included.

Industry/Entity Type

Architect

Coding

Coded - Design and coding required

Number of Pages Required

5+ page

Font styles to use
Sans Serif

Requirements
Must have
• photos should be organized by project - perhaps a summary of photos and then click to enlarge? should be simple to operate. should be able to separate interior design from architecture.
• needs to be easy to add more photos in the future.

```html
<!DOCTYPE html>
<html lang="en">
<head>
<meta charset="utf-8">
<title>bRv Design Group</title>
<link href="https://fonts.googleapis.com/css2?family=Open+Sans:wght@400;600&display=swap" rel="stylesheet">
<style>
:root{
  --dark:#3a3a3c;
  --footer:#3f3f42;
  --teal:#58a9b5;
  --teal-bright:#3ab3c8;
  --heading-teal:#2a9fb8;
  --intro-teal:#3d6b73;
  --grey-band:#cfcfcf;
  --section-bg:#e8e7e5;
  --text:#555;
  --caption:#666;
  --white:#fff;
}
*{margin:0;padding:0;box-sizing:border-box}
html,body{width:788px;height:1200px;overflow:hidden;background:var(--white)}
body{position:relative;font-family:"Open Sans",sans-serif;color:var(--text)}
.abs{position:absolute}
.site-header{left:0;top:0;width:788px;height:38px;background:var(--white)}
.brand{left:0;top:0;width:261px;height:38px;background:var(--dark);display:flex;align-items:center;justify-content:center;color:var(--white);font-size:13px;font-weight:600;letter-spacing:.3px}
.nav-mark{left:303px;top:11px;width:5px;height:5px;border-left:1.5px solid var(--dark);border-top:1.5px solid var(--dark)}
.main-nav{top:15px;left:0;font-size:7px;color:#555;letter-spacing:.3px}
.main-nav span{position:absolute;white-space:nowrap}
.hero{left:0;top:38px;width:788px;height:348px;background:linear-gradient(180deg,#3d6f86 0%,#22485a 45%,#1c2c2a 70%,#1a2418 100%)}
.hero-building{left:210px;top:12px;width:330px;height:250px;background:radial-gradient(ellipse at 50% 55%,#a8782e 0%,#4b4a40 45%,rgba(40,55,60,0) 75%)}
.dots{left:379px;top:371px;display:flex;gap:5px}
.dots i{width:4px;height:4px;border-radius:50%;background:#8a9aa0}
.dots i.on{background:#d6e4ea}
.intro-title{left:0;top:423px;width:788px;text-align:center;font-size:9.5px;color:var(--intro-teal);letter-spacing:.4px}
.intro-text{left:214px;top:446px;width:360px;text-align:center;font-size:6.4px;line-height:9px;color:#666}
.services{left:0;top:503px;width:788px;height:153px}
.services-label{left:0;top:0;width:303px;height:153px;background:var(--grey-band);display:flex;align-items:center;justify-content:center;font-size:14px;color:#111;letter-spacing:.3px}
.services-copy{left:303px;top:0;width:230px;height:153px;background:var(--teal);color:var(--white);padding:23px 30px 0 30px}
.services-copy h3{font-size:7.5px;font-weight:600;letter-spacing:.2px;margin-bottom:5px}
.services-copy p{font-size:6.3px;line-height:8.8px;text-align:justify;margin-bottom:8px}
.services-photo{left:533px;top:0;width:255px;height:153px;background:linear-gradient(120deg,#dcdad4 0%,#f2f1ec 40%,#c9c4ba 75%,#6f6a62 100%)}
.gallery{left:0;top:656px;width:788px;height:483px;background:var(--section-bg)}
.section-mark{width:5px;height:5px;border-left:1.5px solid #222;border-top:1.5px solid #222}
.section-title{font-size:9px;font-weight:600;color:var(--heading-teal);letter-spacing:.3px}
.card{width:133px;height:161px;background:var(--white)}
.card .photo{width:133px;height:114px}
.card .caption{padding:12px 0 0 10px;font-size:7px;line-height:10px;color:var(--caption);letter-spacing:.3px}
.card.highlight{background:var(--teal-bright)}
.card.highlight .photo{background:linear-gradient(180deg,#44b4c6,#3aa9bb)!important;position:relative}
.card.highlight .overlay{position:absolute;left:8px;top:8px;width:120px;color:var(--white);font-size:6.7px;line-height:8.8px}
.card.highlight .caption{color:var(--white)}
.site-footer{left:0;top:1139px;width:788px;height:61px;background:var(--footer);color:#bdbdbd}
.footer-nav{top:20px;font-size:6.5px}
.footer-nav span{position:absolute;white-space:nowrap}
.copyright{left:106px;top:37px;font-size:6.3px;color:#aaa}
.contact{left:526px;top:11px;font-size:6.5px;line-height:13px;color:#aaa}
.social{left:526px;top:43px;display:flex;gap:9px}
.social i{width:9px;height:9px;border-radius:50%;border:1px solid #888}
.footer-brand{left:606px;top:20px;width:102px;text-align:right;font-size:10px;font-weight:600;color:var(--white)}
</style>
</head>
<body>
<header class="site-header abs">
  <div class="brand abs">bRv Design Group</div>
  <div class="nav-mark abs"></div>
  <nav class="main-nav abs">
    <span style="left:309px">HOME</span>
    <span style="left:358px">SERVICES</span>
    <span style="left:419px">ARCHITECTS</span>
    <span style="left:490px">INTERIOR</span>
    <span style="left:551px">PORTFOLIO</span>
    <span style="left:618px">CONTACT US</span>
  </nav>
</header>

<section class="hero abs" role="img" aria-label="Stacked modern house glowing at dusk under a cloudy blue sky, lawn and path in front">
  <div class="hero-building abs"></div>
  <div class="dots abs"><i class="on"></i><i></i><i></i><i></i></div>
</section>

<h1 class="intro-title abs" style="font-weight:400">WE ARE INTRO... WELCOME TO bRv DESIGN GROUP</h1>
<p class="intro-text abs">Ut wisi enim ad minim veniam, quis nostrud exerci tation ullamcorperadipiscing elit, sed diam nonummy nibh&nbsp; suscipit lobortis nisl ut aliquip ex ea commodo consequat.</p>

<section class="services abs">
  <div class="services-label abs">OUR SERVICES</div>
  <div class="services-copy abs">
    <h3>ARCHITECTS &nbsp;|&nbsp; INTERIOR</h3>
    <p>Ut wisi enim ad minim veniam, quis nostrud exerci tation ullamcorperadipiscing elit, sed diam nonummynibh suscipit lobortis nisl ut aliquip ex ea commodo consequat.Ut wisi enim ad minim veniam, quis nostrud exerci tation ullamcorperadipiscing elit, sed diam nonummy</p>
    <p>nibh&nbsp; suscipit lobortis nisl ut aliquip ex ea commodo do consequat.Ut wisi enim ad minim veniam, quis diam nonummy&nbsp; wisi enim ad minim.</p>
  </div>
  <div class="services-photo abs" role="img" aria-label="Bright white living room with sofa, lounge chair and a large window onto the sea"></div>
</section>

<section class="gallery abs">
  <div class="section-mark abs" style="left:106px;top:39px"></div>
  <h2 class="section-title abs" style="left:110px;top:43px">ARCHITECTS</h2>

  <article class="card abs" style="left:106px;top:67px">
    <div class="photo" role="img" aria-label="Modern house with pool and lawn" style="background:linear-gradient(180deg,#8fb6d8 0%,#c6a080 55%,#5e7f3a 100%)"></div>
    <div class="caption">PHASE 1 BUILDING<br>8A HARBOUR BEND RD</div>
  </article>
  <article class="card abs" style="left:254px;top:67px">
    <div class="photo" role="img" aria-label="White apartment block with dark window grid" style="background:linear-gradient(135deg,#bcd2e6 0%,#f0f0f0 45%,#d9d6cf 100%)"></div>
    <div class="caption">PHASE 1 BUILDING<br>8A HARBOUR BEND RD</div>
  </article>
  <article class="card abs" style="left:401px;top:67px">
    <div class="photo" role="img" aria-label="Dark facade with lit glass entrance" style="background:linear-gradient(90deg,#8a7552 0%,#c9b080 35%,#4a4440 70%,#2f2c2a 100%)"></div>
    <div class="caption">PHASE 1 BUILDING<br>8A HARBOUR BEND RD</div>
  </article>
  <article class="card highlight abs" style="left:549px;top:67px">
    <div class="photo" role="img" aria-label="Building project under a teal highlight">
      <p class="overlay">Lorem ispum suscipit lobortis nisl ut aliquip ex ea commodo do consequat.Ut wisi enim ad minim veniam, quis diam nonummy wisi enim ad minim.</p>
    </div>
    <div class="caption">PHASE 1 BUILDING<br>8A HARBOUR BEND RD</div>
  </article>

  <div class="section-mark abs" style="left:106px;top:254px"></div>
  <h2 class="section-title abs" style="left:110px;top:258px">INTERIOR</h2>

  <article class="card abs" style="left:106px;top:282px">
    <div class="photo" role="img" aria-label="Living room with sofa, white table and colourful artwork" style="background:linear-gradient(180deg,#eeeeec 0%,#dcd6cc 60%,#9c6a3e 100%)"></div>
    <div class="caption">PHASE 1 BUILDING<br>8A HARBOUR BEND RD</div>
  </article>
  <article class="card abs" style="left:254px;top:282px">
    <div class="photo" role="img" aria-label="Lounge with dark armchairs and a fireplace" style="background:linear-gradient(180deg,#6f6a70 0%,#3b3536 55%,#8c7a62 100%)"></div>
    <div class="caption">PHASE 1 BUILDING<br>8A HARBOUR BEND RD</div>
  </article>
  <article class="card abs" style="left:401px;top:282px">
    <div class="photo" role="img" aria-label="Dining area with white table and dark shelving" style="background:linear-gradient(180deg,#4a4a4a 0%,#8d8d8d 50%,#e6e6e6 100%)"></div>
    <div class="caption">PHASE 1 BUILDING<br>8A HARBOUR BEND RD</div>
  </article>
  <article class="card abs" style="left:549px;top:282px">
    <div class="photo" role="img" aria-label="Curved timber dining room with sea view windows" style="background:linear-gradient(180deg,#b88d5c 0%,#d8d2c4 45%,#8f7d62 80%,#2a2420 100%)"></div>
    <div class="caption">PHASE 1 BUILDING<br>8A HARBOUR BEND RD</div>
  </article>
</section>

<footer class="site-footer abs">
  <nav class="footer-nav abs" style="left:0">
    <span style="left:106px">Home</span>
    <span style="left:142px">Services</span>
    <span style="left:190px">Architects</span>
    <span style="left:242px">Interior</span>
    <span style="left:284px">Portfolio</span>
    <span style="left:333px">Contact Us</span>
  </nav>
  <p class="copyright abs">© 2014 bRv Design Group, All Rights Reserved.</p>
  <p class="contact abs">info@brvdesignstudio.net<br>(555) 0100 482 36</p>
  <div class="social abs"><i></i><i></i><i></i><i></i></div>
  <div class="footer-brand abs">bRv Design Group</div>
</footer>
</body>
</html>
```